Strong, modern, clean Business Card design

Looking for a stunning, but CLEAN business card design. While we are a faith-based organization, we do NOT want this to look religious.

Industry/Entity Type

Non-Profit

Contact Information for Business Card

Dale Munroe | Lead Pastor
dale@BrightHarvestHope.org
402-555-0148
PO Box 7316
Briarwood, NE 68571

Font styles to use
Serif
Sans Serif

Requirements
Should not have
• Religious imagery or symbolism

```html
<!DOCTYPE html>
<html lang="en">
<head>
<meta charset="utf-8">
<title>Cedar Gate Community – Business Card</title>
<link rel="stylesheet" href="https://fonts.googleapis.com/css2?family=Playfair+Display:wght@400;500&family=Roboto:wght@400;500&family=Roboto+Condensed:wght@700&display=swap">
<style>
  :root {
    --backdrop: #e9e6e1;
    --card-front: #f4f4f4;
    --card-back: #1b1c1e;
    --brand-blue: #4e7f99;
    --ink: #111111;
    --muted: #555a5e;
    --white: #ffffff;
  }
  * { margin: 0; padding: 0; box-sizing: border-box; }
  html, body {
    width: 1200px; height: 960px; overflow: hidden;
    background: var(--backdrop);
  }
  .card {
    position: absolute;
    width: 600px; height: 343px;
    box-shadow: 0 3px 6px rgba(0,0,0,0.25);
  }
  .card--front { left: 313px; top: 113px; background: var(--card-front); }
  .card--back  { left: 311px; top: 472px; background: var(--card-back); }

  .edge-band {
    position: absolute; left: 1px; top: 0; bottom: 0; width: 18px;
    background: var(--brand-blue);
  }
  .edge-rule {
    position: absolute; left: 21px; top: 0; bottom: 0; width: 2px;
    background: var(--ink);
  }

  .wordmark {
    position: absolute; left: 44px; top: 48px;
    font-family: "Playfair Display", serif;
    font-weight: 500;
    color: var(--brand-blue);
    line-height: 1;
  }
  .wordmark__name { font-size: 33px; letter-spacing: 1px; display: block; }
  .wordmark__sub  { font-size: 20px; letter-spacing: 13px; display: block; margin: 8px 0 0 36px; }

  .contact {
    position: absolute; left: 42px; top: 186px;
    font-family: "Roboto", sans-serif;
  }
  .contact__name {
    font-family: "Roboto Condensed", sans-serif;
    font-weight: 700; font-size: 21px; color: var(--brand-blue);
    text-transform: uppercase; line-height: 1;
  }
  .contact__role {
    font-weight: 500; font-size: 15px; color: var(--ink);
    text-transform: uppercase; line-height: 18px; margin: 2px 0 5px 2px;
  }
  .contact__line {
    font-size: 14px; color: var(--muted); line-height: 19.5px;
    display: flex; align-items: center; gap: 8px;
  }
  .contact__line svg { width: 14px; height: 14px; fill: var(--brand-blue); }

  .back-name {
    position: absolute; left: 0; right: 0; top: 118px;
    text-align: center;
    font-family: "Playfair Display", serif;
    font-size: 62px; color: var(--white); line-height: 1;
  }
  .back-url {
    position: absolute; left: 0; right: 0; top: 294px;
    text-align: center;
    font-family: "Roboto", sans-serif;
    font-size: 14px; letter-spacing: 2.4px; color: var(--white);
  }
</style>
</head>
<body>
  <section class="card card--front">
    <div class="edge-band"></div>
    <div class="edge-rule"></div>
    <div class="wordmark">
      <span class="wordmark__name">CEDAR GATE</span>
      <span class="wordmark__sub">COMMUNITY</span>
    </div>
    <div class="contact">
      <p class="contact__name">Dale Munroe</p>
      <p class="contact__role">Lead Pastor</p>
      <p class="contact__line">PO Box 7316</p>
      <p class="contact__line">Briarwood, NE 68571</p>
      <p class="contact__line">
        <svg viewBox="0 0 24 24" aria-hidden="true"><path d="M6.6 10.8a15.1 15.1 0 0 0 6.6 6.6l2.2-2.2a1 1 0 0 1 1-.25 11.4 11.4 0 0 0 3.6.57 1 1 0 0 1 1 1V20a1 1 0 0 1-1 1A17 17 0 0 1 3 4a1 1 0 0 1 1-1h3.5a1 1 0 0 1 1 1c0 1.25.2 2.45.57 3.57a1 1 0 0 1-.25 1z"/></svg>
        402-555-0148
      </p>
      <p class="contact__line">
        <svg viewBox="0 0 24 24" aria-hidden="true"><path d="M2 5h20v14H2z"/><path d="M2 5l10 8 10-8" fill="none" stroke="#f4f4f4" stroke-width="2"/></svg>
        dale@BrightHarvestHope.org
      </p>
    </div>
  </section>

  <section class="card card--back">
    <p class="back-name">Cedar Gate</p>
    <p class="back-url">www.cedargatecommunity.org</p>
  </section>
</body>
</html>
```